Album Artwork Design: Colorado Reggae-Funk-Hip-Hop Band

We're looking for someone to design the album artwork for our new record. The Denver, CO based reggae/rock/hip-hop/jam band is called "B-Roz and the Current". We're looking for front and back panels.

The album is called "Edge of the Lantern", talking about the seasons of life and how its all part of the ride. We were imagining two hands slightly cupped together with a light orb coming out of the palms (or one singular hand). The light has roots that go into the hands and project interesting/psychedelic objects/patterns outward. Potentially a black background.

We're open to other ideas, that was just one the band as a collective thought was cool. Would like it to be colorful and eye-catching but still clean and professional looking.

The Current depicts the band; uplifting, energetic, positive, ect.

Attached below are recordings of the songs, cool album covers we like and some rough logo ideas (please feel free to disregard if you have a better idea). Much thanks for all submissions!

Target Market(s)

Hippies, nature lovers, party people, positive people, music lovers, ect.

Industry/Entity Type

Entertainment

Logo Text

B-Roz and the Current

Requirements
Must have
• Logo for "B-Roz and the Current" - Band name
• Also on the front need "Edge of the Lantern" - Album Name
• Back side needs tracks listings and room for credits:
• 1. Toward Shores We Won't Reach
• 2. Wildflower Over Rivers
• 3. Moon Slides Down
• 4. Alleys of Tamberlin
• 5. We Could Be Free
• 6. Out In Your Glow
• 7. Raise One For Kindness
• Produced & Engineered by Dorian Pellwick & Vellbrook Audio
• © Ruben Ostrander-Hale 2017
• www.brozandthecurrent.example
Nice to have
• Elements of nature (sun, moon, trees, mountains, ect.)
• Psychedelic/visually captivating elements.
• Clean & professional color scheme/branding.
• Should be authentic and have a distinct style.
Should not have
• Anything cheesy & tacky.

```html
<!DOCTYPE html>
<html lang="en">
<head>
<meta charset="utf-8">
<title>B-Roz and the Current – Edge of the Lantern</title>
<link rel="stylesheet" href="https://fonts.googleapis.com/css2?family=Pathway+Gothic+One&display=swap">
<style>
  :root {
    --page: #ffffff;
    --ink-light: #ffffff;
    --ink-ghost: rgba(40, 50, 50, 0.35);
    --teal: #1f6b5e;
    --teal-deep: #143f3a;
    --cream: #f4e6c4;
    --sand: #b89a5c;
    --rock: #8a6a3a;
    --pink: #d9677a;
    --orange: #e98a3c;
    --dusk: #6a4a48;
    --ember: #a0521f;
    --earth: #6b3d1c;
    --fold: rgba(255, 255, 255, 0.55);
  }
  * { box-sizing: border-box; margin: 0; padding: 0; }
  html, body {
    width: 1200px; height: 1200px; overflow: hidden;
    background: var(--page);
    font-family: "Pathway Gothic One", "Arial Narrow", sans-serif;
  }
  .spread {
    position: absolute; left: 20px; top: 310px;
    width: 1160px; height: 580px;
    display: flex;
  }
  .panel { position: relative; width: 580px; height: 580px; overflow: hidden; }
  .panel-photo { position: absolute; inset: 0; }
  .back .panel-photo {
    background:
      radial-gradient(ellipse 60% 40% at 85% 5%, var(--cream), transparent 70%),
      linear-gradient(160deg, var(--teal-deep) 0%, var(--teal) 30%, #5f7f6a 50%, var(--sand) 62%, var(--rock) 80%, #7a6a48 100%);
  }
  .front .panel-photo {
    background:
      radial-gradient(ellipse 50% 30% at 85% 10%, var(--pink), transparent 70%),
      radial-gradient(ellipse 40% 30% at 10% 5%, #f3c48a, transparent 70%),
      linear-gradient(180deg, var(--orange) 0%, #b9708a 22%, var(--dusk) 45%, var(--ember) 62%, var(--earth) 82%, #8a5a20 100%);
  }
  .fold {
    position: absolute; left: 579px; top: 0; height: 580px;
    border-left: 1px dashed var(--fold);
  }
  .ghost-title {
    position: absolute; left: 44px; top: 200px;
    font-size: 58px; letter-spacing: 4px; text-transform: uppercase;
    color: var(--ink-ghost);
  }
  .tracklist {
    position: absolute; left: 44px; top: 290px;
    list-style: none; color: var(--ink-light);
    font-size: 17px; line-height: 26.5px;
  }
  .tracklist li span { text-decoration: underline; text-underline-offset: 2px; }
  .back-logo {
    position: absolute; left: 400px; top: 425px; width: 110px;
    color: var(--ink-light); text-align: center;
    font-size: 22px; line-height: 20px; text-transform: uppercase;
  }
  .back-logo .small { font-size: 13px; line-height: 14px; }
  .credits {
    position: absolute; left: 40px; top: 523px;
    color: var(--ink-light); font-size: 13px; white-space: nowrap;
  }
  .band-name {
    position: absolute; left: 240px; top: 120px; width: 240px;
    color: var(--ink-light); text-align: center; text-transform: uppercase;
    font-size: 64px; line-height: 58px;
  }
  .band-name .small { display: block; font-size: 34px; line-height: 36px; }
  .album-title {
    position: absolute; left: 200px; top: 412px; width: 330px;
    color: var(--ink-light); text-align: center; text-transform: uppercase;
    font-size: 28px; letter-spacing: 3px;
  }
</style>
</head>
<body>
  <main class="spread">
    <section class="panel back">
      <div class="panel-photo" role="img" aria-label="Desert mesa and sandstone cliffs under a stormy teal sky"></div>
      <p class="ghost-title">Edge of the Lantern</p>
      <ol class="tracklist">
        <li>1. <span>Toward Shores We Won't Reach</span></li>
        <li>2. <span>Wildflower Over Rivers</span></li>
        <li>3. <span>Moon Slides Down</span></li>
        <li>4. <span>Alleys of Tamberlin</span></li>
        <li>5. <span>We Could Be Free</span></li>
        <li>6. <span>Out In Your Glow</span></li>
        <li>7. <span>Raise One For Kindness</span></li>
      </ol>
      <p class="back-logo">B-Roz<br><span class="small">and the</span><br>Current</p>
      <p class="credits">Produced &amp; Engineered by Dorian Pellwick &amp; Vellbrook Audio &nbsp;© Ruben Ostrander-Hale 2017 &nbsp;www.brozandthecurrent.example</p>
    </section>
    <section class="panel front">
      <div class="panel-photo" role="img" aria-label="Sunset over a red rock canyon with glowing orange and pink clouds"></div>
      <h1 class="band-name">B-Roz<span class="small">and the</span>Current</h1>
      <h2 class="album-title">Edge of the Lantern</h2>
    </section>
    <div class="fold"></div>
  </main>
</body>
</html>
```